Law Firm Website

We are a small California based law firm specializing in business, corporate and litigation matters. We need to have our website redesigned. We are looking for a new and fresh look for our site, keeping in mind that we are a law firm.
What we don't want:
**the traditional "gavel" and "scales of justice" look
**anything too crazy
What we do want:
**sophisticated yet modern and fresh corporate look and feel
**samples of websites we really like:
http://www.mtrhllp-example.com
http://www.orwenlatch-example.com/
we also like:
http://www.verdtolbain-example.com/
http://www.qh-example.com/
http://www.pembrost-example.com/
http://www.nvtr-example.com
http://www.rmqlaw-example.com/
The content will be whatever is currently on our website (www.halvencourtlaw-example.com). We will be selecting the winner based on originality and keeping the above requirements in mind. Please note that the photos that you use will be the ones that we will be using, so choose wisely because the photos will make a difference.
Target Market(s)
Corporate clients
Industry/Entity Type
Law Firm
Look and feel

```html
<!DOCTYPE html>
<html lang="en">
<head>
<meta charset="utf-8">
<title>Halvencourt Law Group, LLP</title>
<link href="https://fonts.googleapis.com/css2?family=Bitter:ital,wght@0,400;0,700;1,400;1,700&family=Open+Sans:wght@400;600;700&display=swap" rel="stylesheet">
<style>
:root{
  --blue:#1d6fd0;
  --blue-dark:#0d4a8f;
  --navy:#0e3f7a;
  --band:#1b63b5;
  --text:#333;
  --muted:#777;
  --rule:#d9d9d9;
  --gold:#f5b400;
  --light:#f4f4f4;
}
*{box-sizing:border-box;margin:0;padding:0}
html,body{width:941px;height:1200px;overflow:hidden}
body{position:relative;background:#fff;font-family:'Open Sans',Arial,sans-serif;color:var(--text)}
.abs{position:absolute}
.topbar{left:0;top:0;width:941px;height:22px;background:#f1f1f1;border-bottom:1px solid #e2e2e2}
.topbar .phone{right:98px;top:0;height:22px;width:146px;background:#fafafa;border-left:1px solid #ddd;border-right:1px solid #ddd;font-size:11px;color:#888;display:flex;align-items:center;gap:8px;padding-left:10px}
.header{left:0;top:22px;width:941px;height:80px;background:linear-gradient(#fff,#f2f2f2)}
.brand{left:80px;top:32px;display:flex;gap:8px;align-items:flex-start}
.brand-mark{width:64px;height:64px;background:var(--blue)}
.brand-name{font-family:'Bitter',serif;font-size:19px;color:var(--blue-dark);line-height:1.2;margin-top:3px}
.brand-tag{font-family:'Bitter',serif;font-size:14px;color:#333;margin-top:2px}
.nav{left:487px;top:76px;display:flex;font-family:'Bitter',serif;font-size:12px;color:#333}
.nav a{color:inherit;text-decoration:none;height:26px;display:flex;align-items:center;padding:0 12px}
.nav a.on{background:var(--blue-dark);color:#fff;font-weight:700}
.nav a+a{margin-left:6px}
.hero{left:0;top:102px;width:941px;height:302px;background:linear-gradient(180deg,#1554a3 0 6px,#2a7ddb 6px,#2b80de 60%,#4b92e2)}
.hero h1{left:0;top:52px;width:941px;text-align:center;font-family:'Bitter',serif;font-weight:700;font-size:24px;color:var(--blue);-webkit-text-stroke:1.2px #fff;paint-order:stroke}
.hero p{left:140px;top:92px;width:661px;text-align:center;font-family:'Bitter',serif;font-size:17.5px;line-height:20px;color:#fff}
.consult{left:263px;top:172px;width:414px;height:130px;background:rgba(14,63,122,.92)}
.consult h2{left:11px;top:9px;font-size:20px;font-weight:600;color:#fff;font-family:'Open Sans',sans-serif}
.field{background:#fff;font-size:9px;color:#333;padding:4px 5px;position:absolute}
.submit{left:341px;top:102px;width:59px;height:17px;border-radius:9px;background:linear-gradient(#ffd94a,var(--gold));font-size:10px;font-weight:700;color:var(--navy);text-align:center;line-height:17px}
.welcome{left:81px;top:424px;width:497px}
.welcome h2,.testi h2{font-family:'Bitter',serif;font-weight:400;font-size:19px;color:var(--blue-dark)}
.welcome p{font-family:Arial,sans-serif;font-size:9.6px;line-height:15.6px;margin-top:12px}
.btn{display:inline-block;height:19px;padding:0 9px;border-radius:10px;background:linear-gradient(#3a86dd,#0f4e99);color:#fff;font-size:10.5px;font-weight:600;line-height:19px;text-align:center}
.vline{left:588px;top:430px;width:1px;height:168px;background:var(--rule)}
.testi{left:608px;top:424px;width:249px;height:170px;background:#fafafa}
.testi .all{right:6px;top:14px;font-family:'Bitter',serif;font-style:italic;font-size:9px}
.testi blockquote{left:4px;top:37px;width:240px;font-family:'Bitter',serif;font-style:italic;font-size:9.2px;line-height:16px;padding-left:14px}
.hr{left:88px;top:621px;width:761px;height:1px;background:var(--rule)}
.att-title{left:0;top:632px;width:941px;text-align:center;font-family:'Bitter',serif;font-size:25px;color:var(--blue-dark)}
.att-sub{left:0;top:668px;width:941px;text-align:center;font-family:'Bitter',serif;font-size:11.5px}
.card{top:712px;width:170px;text-align:center}
.card .photo{width:150px;height:150px;margin:0 auto;border-radius:50%;border:6px solid #eee;box-shadow:0 1px 3px rgba(0,0,0,.25)}
.card h3{margin-top:18px;font-family:'Bitter',serif;font-weight:400;font-size:17px;color:#333}
.card p{margin-top:6px;font-size:9.2px;line-height:14px;color:var(--muted)}
.card p b{color:#333;font-weight:600}
.card .btn{margin-top:10px}
.dots{top:712px;width:0;height:268px;border-left:1px dotted #ccc}
.footer{left:0;top:1028px;width:941px;height:134px;background:var(--band);border-top:5px solid var(--navy)}
.panel{left:96px;top:10px;width:749px;height:124px;background:#1a5fb0;border:1px solid #2d74c5}
.tabs{left:0;top:0;display:flex}
.tabs span{height:25px;padding:0 8px;line-height:25px;color:#fff;font-size:13.5px;border-right:1px solid #2d74c5;background:#1656a3}
.tabs span.on{background:var(--navy)}
.panel p,.panel .col{color:#fff;font-size:8.8px;line-height:15px}
.map{left:556px;top:31px;width:186px;height:72px;background:linear-gradient(135deg,#e8ecd9,#bcd3ea)}
.legal{left:88px;top:1168px;font-size:9px;line-height:14.5px;color:#444}
.foot-brand{right:73px;top:1168px;display:flex;gap:6px;align-items:flex-start}
.foot-brand .sq{width:28px;height:28px;background:#8a9bb0}
.foot-brand .n{font-family:'Bitter',serif;font-size:9px;color:#555}
.foot-brand .t{font-family:'Bitter',serif;font-size:7px;color:#555}
</style>
</head>
<body>
<div class="abs topbar">
  <div class="abs phone">
    <svg width="14" height="12" viewBox="0 0 14 12"><path d="M1 4c0-2 3-3 6-3s6 1 6 3v1h-3V3.5H4V5H1z M3 6h8l1 5H2z" fill="#c9c9c9"/></svg>
    1 - 800 - 555 - 0148
  </div>
</div>

<header class="abs header"></header>
<div class="abs brand">
  <div class="brand-mark"></div>
  <div>
    <div class="brand-name">Halvencourt Law Group, LLP</div>
    <div class="brand-tag">Attorneys at Law</div>
  </div>
</div>
<nav class="abs nav">
  <a class="on">Home</a><a>About HLG</a><a>Practice Areas</a><a>Links</a><a>Contact</a>
</nav>

<section class="abs hero" role="img" aria-label="Blue-toned city skyline with high-rise office towers">
  <h1 class="abs">Corporate/M&amp;A Law Firm of the Year</h1>
  <p class="abs">Halvencourt Law Group, LLP provides quality legal representation to corporate as well as individual clients in the areas of business, corporate,</p>
  <form class="abs consult">
    <h2 class="abs">Requesting a Free Consultation</h2>
    <div class="field" style="left:13px;top:44px;width:188px;height:19px">Name:</div>
    <div class="field" style="left:13px;top:72px;width:188px;height:19px">E-mail:</div>
    <div class="field" style="left:13px;top:100px;width:188px;height:19px">Phone:</div>
    <div class="field" style="left:213px;top:44px;width:188px;height:51px">Message:</div>
    <div class="abs submit">Submit</div>
  </form>
</section>

<section class="abs welcome">
  <h2>Welcome to Halvencourt Law Group, LLP</h2>
  <p><b><i>Our attorneys are committed to providing zealous advocacy in litigation, as well as creative approaches to difficult challenges that face our business clients.</i></b> Our goal is to provide the highest level of representation and personal service to each and every client, and to meet and exceed each client's expectations. We take the time to explore and explain all viable options and keep our clients informed at every step of their legal matter.</p>
  <p style="margin-top:15px">We encourage you to contact us to discuss the development of a professional relationship. If you seek a firm that is experienced and committed to representing your best interests, then look no further.</p>
  <div style="text-align:right;margin-top:10px"><span class="btn" style="width:64px">Readmore</span></div>
</section>
<div class="abs vline"></div>

<aside class="abs testi">
  <h2 style="position:absolute;left:6px;top:2px">Testimonials</h2>
  <span class="abs all">View All &gt;&gt;</span>
  <blockquote class="abs"><svg style="position:absolute;left:2px;top:4px" width="10" height="8" viewBox="0 0 10 8"><path d="M0 8V4l2-4h2L3 4h1v4zM6 8V4l2-4h2L9 4h1v4z" fill="#666"/></svg>Marlowe Law Group is a bankruptcy firm that including San Francisco, Oakland, Fremont, and San Jose.&nbsp; Clients need to declare</blockquote>
  <div class="abs" style="left:0;top:97px;width:241px;height:1px;background:#bbb"></div>
  <div class="abs" role="img" aria-label="Portrait photo of the client" style="left:3px;top:114px;width:58px;height:52px;background:linear-gradient(#ddd,#999);border:1px solid #ccc"></div>
  <div class="abs" style="left:71px;top:112px;font-family:'Bitter',serif;font-style:italic;font-weight:700;font-size:12px">Daniel Arbor, USA,</div>
  <div class="abs" style="left:71px;top:130px;font-family:'Bitter',serif;font-style:italic;font-size:8px;color:#aaa">Account Manager of QRN Ltd.,</div>
</aside>

<div class="abs hr"></div>
<h2 class="abs att-title" style="font-weight:400">Attorneys at Law</h2>
<p class="abs att-sub">Ipsum is simply dummy text of the printing and typesetting</p>

<div class="abs card" style="left:77px">
  <div class="photo" role="img" aria-label="Attorney seated at an office window" style="background:linear-gradient(135deg,#dfe6ea,#8d9aa3)"></div>
  <h3>Alan Brooks</h3>
  <p><b>Lorem ipsum dolor sit amet, consectetur adipisicing elit, sed do</b> eiusmod tempor incididunt ut labore et dolore magna aliqua.</p>
  <span class="btn" style="width:64px">Readmore</span>
</div>
<div class="abs dots" style="left:259px"></div>
<div class="abs card" style="left:289px">
  <div class="photo" role="img" aria-label="Attorney in suit before a bookshelf and flag" style="background:linear-gradient(135deg,#8b5a3a,#2b2320)"></div>
  <h3>Peter Vance</h3>
  <p><b>Lorem ipsum dolor sit amet, consectetur adipisicing elit, sed do</b> eiusmod tempor incididunt ut labore et dolore magna aliqua.</p>
  <span class="btn" style="width:64px">Readmore</span>
</div>
<div class="abs dots" style="left:468px"></div>
<div class="abs card" style="left:494px">
  <div class="photo" role="img" aria-label="Portrait of attorney in dark jacket" style="background:linear-gradient(135deg,#a0522d,#2a1a14)"></div>
  <h3>Rina Solano</h3>
  <p><b>Lorem ipsum dolor sit amet, consectetur adipisicing elit, sed do</b> eiusmod tempor incididunt ut labore et dolore magna aliqua.</p>
  <span class="btn" style="width:64px">Readmore</span>
</div>
<div class="abs dots" style="left:668px"></div>
<div class="abs card" style="left:690px">
  <div class="photo" role="img" aria-label="Senior attorney speaking in a courtroom" style="background:linear-gradient(135deg,#6b5a48,#1e1a17)"></div>
  <h3>Joel Ricard</h3>
  <p><b>Lorem ipsum dolor sit amet, consectetur adipisicing elit, sed do</b> eiusmod tempor incididunt ut labore et dolore magna aliqua.</p>
  <span class="btn" style="width:64px">Readmore</span>
</div>

<footer class="abs footer">
  <div class="abs panel">
    <div class="abs tabs"><span class="on">San Mateo</span><span style="padding:0 12px">San Francisco</span><span style="padding:0 13px">San Jose</span></div>
    <p class="abs" style="left:10px;top:32px;width:530px">Our main office is located in San Mateo, right off the 101 and 92 highway. The building has plenty of free parking and you can always leave documents with the receptionist. If you are in need of a bankruptcy lawyer in San Jose, please contact us today.</p>
    <div class="abs col" style="left:9px;top:68px;font-weight:700">Lindenport Office<br>4100 Harbor Point Drive, 8th Floor<br>Lindenport, California 90000</div>
    <div class="abs col" style="left:195px;top:73px;font-weight:700">Telephone: (949) 555-0120<br>Facsimile:&nbsp;&nbsp; (949) 555-0127</div>
    <div class="abs col" style="left:347px;top:73px;font-weight:700">E-Mail for general inquiries:<br>info@halvencourtlaw-example.com</div>
    <div class="abs map" role="img" aria-label="Street map of the San Mateo office location"></div>
    <div class="abs" style="left:684px;top:106px;font-size:8.5px;color:#cfe0f5">&#9906; View large</div>
  </div>
</footer>

<div class="abs legal">© 2014 halvencourtlaw All Right Reserved &nbsp;|&nbsp; Private Policy &nbsp;|&nbsp; Terms &amp; Conditions<br>Attorney Advertising. Prior results do not guarantee a similar outcome.</div>
<div class="abs foot-brand">
  <div class="sq"></div>
  <div><div class="n">Halvencourt Law Group, LLP</div><div class="t">Attorneys at Law</div></div>
</div>
</body>
</html>
```